Help Design the Packaging for our Nicotine Replacement Therapy

Packaging Design Brief for Brevalo
We are using this contest to find a designer who can design the packaging for the full line of products listed below for our new brand. This contest will require you to provide designs for the Traditional mint in both the 2mg and 4mg, and the Traditional Cinnamon 2 mg and 4mg, plus the mint in the Modern, 2mg and 4mg. We would like to see how you propose to tie the designs together so their is clear differentiate between the products and flavors, yet it maintains brand cohesiveness.
We would like to then work with the contest winner on a 1-1 project to develop the packaging for the remaining products.
Project Overview:
Brevalo is launching a new line of nicotine replacement therapy (NRT) products, including gum and lozenges in multiple flavors and strengths. The packaging design needs to reflect Brevalo’s brand values of trust, warmth, professionalism, and customer-centricity while being visually appealing, functional, and easily distinguishable.
Here is our full product line up so you can design product packaging that has the potential to expand as we add more flavors.
Product Line-Up:
1. Nicotine Gum ("Traditional" because it tastes and feels like hollbrun's gum):
- Flavors: Mint, Fruit, Cinnamon
- Strengths: 2mg, 4mg
- Pack Size: 240 pieces per pack
2. Nicotine Gum (Stiffer, Playdough-Like Texture will be called "Classic"):
- Strengths: 2mg, 4mg
3. Nicotine Lozenges:
- Flavors: Mint, Citrus, Berry
- Strengths: 2mg, 4mg
- Pack Size: 120 pieces per pack
Design Objectives:
1. Brand Consistency:
- The Brevalo logo should be easily recognizable across all packaging.
- The design should reflect the brand’s personality: trustworthy, professional, warm, and approachable.
- Packaging should evoke a sense of reliability and comfort, appealing to a mature audience.
2. Differentiation:
- Flavor Differentiation:
- Use distinct colors for each flavor to ensure they are easily distinguishable.
- Incorporate icons or images that represent the flavor (e.g., mint leaves for Mint, cinnamon sticks for Cinnamon).
- Strength Differentiation:
- Clearly display the nicotine strength (2mg or 4mg) in a way that stands out at a glance.
- Gum Texture Differentiation:
- Create a visual distinction between the traditional chewing gum and the stiffer, playdough-like gum while maintaining a cohesive brand look.
- Consider using different background textures, patterns, or additional design elements to indicate the different textures while ensuring they still feel part of the same family.
3. Product Type Differentiation:
- Gum vs. Lozenges:
- The lozenges should be visually distinct from the gum products while still fitting within the overall Brevalo brand aesthetic.
- Consider using a different shape or design element on the lozenge packaging (e.g., a lozenge icon or a unique pattern) to differentiate them from the gum.
- Maintain consistent use of colors for flavors across both gum and lozenge packaging (e.g., Mint gum and Mint lozenges should share the same color scheme) to unify the product line.
4. Scalability:
- The design should be flexible enough to accommodate additional flavors or product variations in the future.
- Ensure that any new flavor or product type can be easily integrated into the existing design template.
Content Requirements:
1. Front of Pack:
- Brevalo logo
- Flavor name and representative image
- Nicotine strength (2mg or 4mg)
- Indication of gum type (Traditional or Stiffer texture)
- Pack size (e.g., "240 Pieces")
2. Here are the die lines from the manufacturer. You will see that there are certain things that must be included on the gum packaging:
https://files.parvendo.net/folders/7qtr82Km_X4p61TzBn5vedLpQw9aY3R?usp=share_link
Overall Feel:
- The packaging should communicate that Brevalo is a trustworthy, professional brand with a warm, supportive approach. It should feel modern and appeal to a broad audience both male and female.
Packaging design for all SKUs listed above, with clear differentiation between flavors, strengths, and product types.
Here is the link to the brevalo logo. https://files.parvendo.net/file/d/5-RHwtMbqpt213GjwuvraxH8LkZ4QE9BY/view?usp=sharing We are not opposed to the color of the dots and + sign changing to signify flavor either.
Target Market(s)
individuals 18-55+ looking to quit vaping and smoking
Industry/Entity Type
nicotine replacement therapy
Font styles to use
Other font styles liked:
- should compliment and look good with our logo and font which is Nexa bold
Requirements
Must have
- we want to look professional and trustworthy. . .and we want a design that is cohesive across the product set and can expand and stay on brand with additional flavors.
Nice to have
- We will pick a winner and then pay that winner to do the rest of the package designs for each sku and lozenges too.

```html
<!DOCTYPE html>
<html lang="en">
<head>
<meta charset="utf-8">
<title>Brevalo Nicotine Gum Packaging – Stiffer and Traditional Mint</title>
<link rel="stylesheet" href="https://fonts.googleapis.com/css2?family=Montserrat:wght@400;500;700;800&display=swap">
<style>
  :root {
    --canvas: #ffffff;
    --green-base: #7a9b62;
    --green-deep: #6a8a52;
    --green-muted: #768a66;
    --green-light: #98b07f;
    --panel-light: #ffffff;
    --panel-shade: #e2e2e2;
    --ink: #111111;
    --ink-soft: #555555;
    --caption: #333333;
    --leaf-soft: #e6eee0;
    --leaf-mid: #c9dabd;
    --leaf-edge: #b7cca8;
    --accent: #3bb54a;
  }
  * { box-sizing: border-box; margin: 0; padding: 0; }
  html, body {
    width: 1200px; height: 900px; overflow: hidden;
    background: var(--canvas);
    font-family: "Montserrat", Arial, sans-serif;
  }
  .canvas { position: relative; width: 1200px; height: 900px; }

  .pack {
    position: absolute;
    width: 392px; height: 477px;
    box-shadow: 0 3px 4px rgba(0,0,0,0.18);
    overflow: hidden;
  }
  .pack--stiffer { left: 115px; top: 63px; }
  .pack--traditional { left: 725px; top: 65px; }

  .pack__band {
    position: absolute; left: 0; top: 0; width: 100%;
  }
  .pack--stiffer .pack__band {
    height: 190px;
    background: radial-gradient(ellipse at 50% 50%, var(--green-base) 0%, var(--green-deep) 100%);
  }
  .pack--traditional .pack__band {
    height: 193px;
    background: linear-gradient(180deg,
      var(--green-base) 0%,
      var(--green-muted) 30%,
      var(--green-light) 50%,
      var(--green-muted) 72%,
      var(--green-light) 100%);
  }

  .pack__variant {
    position: absolute; left: 0; width: 100%;
    text-align: center;
    color: #ffffff;
    font-weight: 500;
    font-size: 22px;
    letter-spacing: 3px;
    line-height: 1;
  }
  .pack--stiffer .pack__variant { top: 103px; }
  .pack--traditional .pack__variant { top: 106px; }

  .pack__panel {
    position: absolute; left: 0; bottom: 0; width: 100%;
    background: linear-gradient(90deg, var(--panel-light) 0%, #f7f7f7 55%, var(--panel-shade) 100%);
  }
  .pack--stiffer .pack__panel { top: 190px; }
  .pack--traditional .pack__panel { top: 193px; }

  .brand {
    position: absolute; left: 66px; top: 34px;
    display: flex; align-items: center; gap: 8px;
  }
  .brand__mark {
    width: 14px; height: 14px; border-radius: 50%;
    background: var(--accent);
  }
  .brand__name {
    font-weight: 700; font-size: 58px; line-height: 1;
    color: var(--ink); letter-spacing: -0.5px;
  }
  .product-type {
    position: absolute; left: 75px; top: 105px;
    font-size: 15px; font-weight: 400; letter-spacing: 0.4px;
    color: var(--ink-soft);
  }
  .flavor-art {
    position: absolute; left: 168px; top: 145px;
    width: 98px; height: 92px;
    border-radius: 46% 54% 50% 50%;
    background: radial-gradient(circle at 50% 45%, var(--leaf-soft) 0%, var(--leaf-mid) 70%, var(--leaf-edge) 100%);
  }
  .pack__stat {
    position: absolute; bottom: 14px;
    font-weight: 800; color: var(--ink); line-height: 1;
    text-align: center;
  }
  .pack__stat-value { display: block; font-size: 15px; }
  .pack__stat-label { display: block; font-size: 7.5px; letter-spacing: 0.3px; margin-top: 2px; }
  .pack__stat--count { left: 40px; }
  .pack__stat--strength { right: 28px; }

  .caption {
    position: absolute; width: 320px; text-align: center;
    font-weight: 700; font-size: 26px; line-height: 37px;
    color: var(--caption);
  }
  .caption--stiffer { left: 150px; top: 695px; }
  .caption--traditional { left: 773px; top: 693px; }
</style>
</head>
<body>
<main class="canvas">

  <section class="pack pack--stiffer" aria-label="Stiffer mints pack front">
    <div class="pack__band" role="img" aria-label="Green band with a scattered triangle texture pattern"></div>
    <p class="pack__variant">STIFFER MINTS</p>
    <div class="pack__panel">
      <div class="brand"><span class="brand__mark"></span><span class="brand__name">Brevalo</span></div>
      <p class="product-type">NICOTINE GUMS</p>
      <div class="flavor-art" role="img" aria-label="Mint leaf illustration"></div>
      <p class="pack__stat pack__stat--count"><span class="pack__stat-value">240</span><span class="pack__stat-label">MINTS</span></p>
      <p class="pack__stat pack__stat--strength"><span class="pack__stat-value">4MG</span><span class="pack__stat-label">STRENGTH</span></p>
    </div>
  </section>

  <section class="pack pack--traditional" aria-label="Traditional mints pack front">
    <div class="pack__band" role="img" aria-label="Green band with a soft flowing wave pattern"></div>
    <p class="pack__variant">TRADITIONAL MINTS</p>
    <div class="pack__panel">
      <div class="brand"><span class="brand__mark"></span><span class="brand__name">Brevalo</span></div>
      <p class="product-type">NICOTINE GUMS</p>
      <div class="flavor-art" role="img" aria-label="Mint leaf illustration"></div>
      <p class="pack__stat pack__stat--count"><span class="pack__stat-value">240</span><span class="pack__stat-label">MINTS</span></p>
      <p class="pack__stat pack__stat--strength"><span class="pack__stat-value">4MG</span><span class="pack__stat-label">STRENGTH</span></p>
    </div>
  </section>

  <p class="caption caption--stiffer">Design 1<br>(stiffer)</p>
  <p class="caption caption--traditional">Design 2<br>(traditional)</p>

</main>
</body>
</html>
```